New River III Precinct 6x11 GOTV postcard

We require BOTH persuasive copy and high-impact layout for an oversized 6x11 political mailer. This might be one person, but it likely requires a specialized "creative team." of an experienced political strategist copywriter PLUS a graphic designer - so the words fit the exact layout block, and the visuals reinforce the psychological punch of the headline.

The goal is to remove all excuses a targeted audience of ~900 registered Democratic + ~1800 Unaffiliated voters in our precinct - have for not voting.

I need to be able to work by phone / online chat to iterate designs
I need to own the design in the top couple of software outputs that any printer service will require.

I want to experiment with very subtle background images as follows:
- Front of postcard that conveys "CHANGE" of not just seasons - but of encouraging change of precinct voter representation - so anything about fall foliage / conveyance of change tie-in is worthy of considering
- Back of postcard - any Appalachian long rage mountain view that includes 5-7 layers of hills in the distance.
Some photos as samples to consider.

Target Market(s)

~2,700 registered Democrats and Unaffiliated voters

Requirements
Must have
• We require BOTH persuasive copy and high-impact layout for an oversized 6x11 political mailer. This might be one person, but it likely requires a specialized "creative team." of an experienced political strategist copywriter PLUS a graphic designer - so the words fit the exact layout block, and the visuals reinforce the psychological punch of the headline
Nice to have
• subtle background photos

```html
<!DOCTYPE html>
<html lang="en">
<head>
<meta charset="UTF-8">
<title>Vote for Change – Precinct Mailer</title>
<link href="https://fonts.googleapis.com/css2?family=Oswald:wght@500;600&family=Open+Sans:ital,wght@0,400;0,600;0,700;1,700&family=Pinyon+Script&display=swap" rel="stylesheet">
<style>
:root{
  --red:#a61e23;
  --navy:#141a46;
  --gold:#f2a51f;
  --rule:#f0a530;
  --ink:#1d1d1f;
  --pink:#e5407f;
  --paper:#ffffff;
}
*{box-sizing:border-box;margin:0;padding:0}
html,body{width:1200px;height:667px;overflow:hidden;background:#fff}
.mailer{position:relative;width:1200px;height:667px;border:2px solid var(--pink);background:#fff;overflow:hidden;font-family:"Open Sans",Arial,sans-serif;color:var(--ink)}
.headline-band{position:absolute;left:13px;top:13px;width:1174px;height:74px;background:var(--red);border-top:1px solid #333;display:flex;align-items:center;justify-content:center;gap:32px;color:#fff}
.headline-band h1{font-family:Oswald,sans-serif;font-weight:600;font-size:33px;letter-spacing:.2px;transform:scaleY(1.08)}
.stars{display:flex;gap:10px}
.stars svg{width:22px;height:22px;fill:#fff}
.mountain-backdrop{position:absolute;left:13px;top:380px;width:1174px;height:205px;background:linear-gradient(180deg,#ffffff 0%,#dfe9ef 22%,#a9c3d3 45%,#6e98b3 70%,#3f6e90 100%)}
.footer-band{position:absolute;left:13px;top:581px;width:1174px;height:74px;background:var(--navy);display:flex;align-items:center;justify-content:center;gap:20px}
.footer-band .slogan{font-family:Oswald,sans-serif;font-weight:500;font-size:28px;letter-spacing:2px;color:#fff}
.slogan .future{color:var(--gold)}
.slogan .vote{color:#d6262b}
.footer-band .divider{width:3px;height:30px;background:#fff;margin:0 18px}
.footer-band .tagline{font-family:"Pinyon Script",cursive;font-size:27px;color:#fff}
.tagline .lead{color:var(--gold)}
.footer-band .star svg{width:24px;height:24px;fill:var(--gold);display:block}
.panel{position:absolute;background:#fff;border:2px solid var(--navy);border-radius:16px;overflow:hidden}
.panel-head{background:var(--navy);color:#fff;text-align:center}
.pain-panel{left:42px;top:105px;width:394px;height:450px}
.pain-panel .panel-head{height:51px;padding-top:2px}
.pain-panel h2{font-family:"Open Sans",sans-serif;font-weight:700;font-size:18px;line-height:20px}
.pain-panel h2 em{font-style:italic}
.pain-panel .sub{font-size:11.5px;font-weight:600;line-height:13px}
.issue{display:flex;margin-left:6px}
.issue .icon{width:62px;flex:none;display:flex;align-items:center;justify-content:center}
.issue .icon svg{width:44px;height:44px;fill:var(--navy)}
.issue .copy{flex:1;margin-right:6px;padding:8px 14px 4px 6px;border-bottom:1.5px solid var(--rule)}
.issue:last-child .copy{border-bottom:none}
.issue h3,.topic h3{font-family:Oswald,sans-serif;font-weight:500;font-size:16px;color:var(--red);line-height:18px;letter-spacing:.2px}
.issue p{font-size:13px;line-height:15px;letter-spacing:.8px;text-align:justify}
.topics-panel{left:449px;top:107px;width:311px;height:448px;padding:0 6px}
.topic{border-bottom:1.5px solid var(--rule);padding:8px 5px 7px}
.topic:last-child{border-bottom:none}
.topic .title{display:flex;align-items:flex-end;gap:8px;margin-bottom:4px}
.topic .title svg{width:32px;height:32px;fill:var(--red)}
.topic p{font-size:13px;line-height:15px;text-align:justify}
.ballot-panel{left:774px;top:111px;width:385px;height:444px}
.ballot-panel .panel-head{height:46px;display:flex;align-items:center;justify-content:center}
.ballot-panel h2{font-family:Oswald,sans-serif;font-weight:500;font-size:17px;letter-spacing:.6px}
.ballot{list-style:none;padding:9px 12px 0 8px}
.ballot li{display:flex;align-items:baseline;height:25.2px;font-family:Oswald,sans-serif;font-weight:500;font-size:12.5px;color:var(--navy)}
.ballot .bullet{color:var(--red);width:19px;flex:none;font-size:13px}
.ballot .leader{flex:1;border-bottom:1.5px dotted var(--navy);margin:0 3px;transform:translateY(-3px)}
.ballot .choice{color:var(--red)}
</style>
</head>
<body>
<div class="mailer">
  <header class="headline-band">
    <div class="stars" aria-hidden="true">
      <svg viewBox="0 0 24 24"><path d="M12 1l3.2 7.2 7.8.7-5.9 5.2 1.8 7.7L12 17.8l-6.9 4 1.8-7.7L1 8.9l7.8-.7z"/></svg>
      <svg viewBox="0 0 24 24"><path d="M12 1l3.2 7.2 7.8.7-5.9 5.2 1.8 7.7L12 17.8l-6.9 4 1.8-7.7L1 8.9l7.8-.7z"/></svg>
      <svg viewBox="0 0 24 24"><path d="M12 1l3.2 7.2 7.8.7-5.9 5.2 1.8 7.7L12 17.8l-6.9 4 1.8-7.7L1 8.9l7.8-.7z"/></svg>
    </div>
    <h1>THIS NOVEMBER HOLD THEM ACCOUNTABLE – VOTE FOR CHANGE</h1>
    <div class="stars" aria-hidden="true">
      <svg viewBox="0 0 24 24"><path d="M12 1l3.2 7.2 7.8.7-5.9 5.2 1.8 7.7L12 17.8l-6.9 4 1.8-7.7L1 8.9l7.8-.7z"/></svg>
      <svg viewBox="0 0 24 24"><path d="M12 1l3.2 7.2 7.8.7-5.9 5.2 1.8 7.7L12 17.8l-6.9 4 1.8-7.7L1 8.9l7.8-.7z"/></svg>
      <svg viewBox="0 0 24 24"><path d="M12 1l3.2 7.2 7.8.7-5.9 5.2 1.8 7.7L12 17.8l-6.9 4 1.8-7.7L1 8.9l7.8-.7z"/></svg>
    </div>
  </header>

  <div class="mountain-backdrop" role="img" aria-label="Soft blue Appalachian long-range mountain view with layered ridgelines"></div>

  <section class="panel pain-panel">
    <div class="panel-head">
      <h2><em>INTENTIONAL</em> LOCAL PAIN</h2>
      <p class="sub">to avoid accountability, they’ve cleverly delayed<br>many / most impacts until&nbsp; AFTER the 2026 election.</p>
    </div>
    <div class="issue">
      <div class="icon"><svg viewBox="0 0 48 48"><circle cx="12" cy="12" r="5"/><circle cx="36" cy="12" r="5"/><circle cx="24" cy="16" r="6"/><path d="M3 34v-8a6 6 0 016-6h6a6 6 0 015 3 8 8 0 00-4 7v4zM45 34v-8a6 6 0 00-6-6h-6a6 6 0 00-5 3 8 8 0 014 7v4zM14 40v-9a6 6 0 016-6h8a6 6 0 016 6v9z"/></svg></div>
      <div class="copy"><h3>FAMILY BUDGET</h3><p>exploded costs for everything: groceries, gas, car insurance, rent</p></div>
    </div>
    <div class="issue">
      <div class="icon"><svg viewBox="0 0 48 48"><path d="M24 3a21 21 0 110 42 21 21 0 010-42zm0 5a16 16 0 100 32 16 16 0 000-32zm-3 6h6v7h7v6h-7v7h-6v-7h-7v-6h7z"/></svg></div>
      <div class="copy"><h3>HEALTH</h3><p>Expired subsidies, tax credits means 1 million families in NC will lose coverage or pay more. 50% cuts to hospitals, mental health facilities; rural facilities will be closing.</p></div>
    </div>
    <div class="issue">
      <div class="icon"><svg viewBox="0 0 48 48"><path d="M31 3h12v12h-4V9.8l-6.3 6.3A13 13 0 0123 36.9V40h5v4h-5v4h-4v-4h-5v-4h5v-3.1a13 13 0 0110.7-23.8L36 6.9V7h-5zM21 15a9 9 0 100 18 9 9 0 000-18z"/></svg></div>
      <div class="copy"><h3>REPRODUCTIVE RIGHTS</h3><p>Government authoritarian intrusion censor women’s rights</p></div>
    </div>
    <div class="issue">
      <div class="icon"><svg viewBox="0 0 48 48"><path d="M24 3a21 21 0 110 42 21 21 0 010-42zm0 4a17 17 0 100 34 17 17 0 000-34zM15 12h2v8h1v-8h2v8h1v-8h2v9a4 4 0 01-3 4v13h-3V25a4 4 0 01-3-4zm15 0c3 0 4 5 4 10v4h-2v12h-3V14a2 2 0 011-2z"/></svg></div>
      <div class="copy"><h3>FOOD SECURITY</h3><p>Weaponized hunger – cuts to SNAP; school meals cut; additional work requirements.</p></div>
    </div>
    <div class="issue">
      <div class="icon"><svg viewBox="0 0 48 48"><path d="M24 3l20 8-20 8-20-8zm-11 12l11 5 11-5v6a11 11 0 01-22 0zm25 2h2v9h-2zM9 46c0-8 5-13 10-14l5 6 5-6c5 1 10 6 10 14z"/></svg></div>
      <div class="copy"><h3>EDUCATION</h3><p>Laurel County $2.2mm shortfall personnel cuts, freezes in hiring, teacher training. Abandoning civil rights of Special Ed students to HHS and DOL.</p></div>
    </div>
  </section>

  <section class="panel topics-panel">
    <div class="topic">
      <div class="title"><svg viewBox="0 0 32 32"><path d="M16 2l15 13h-4v15H5V15H1zM7 3h4v4l-4 3zM9 18v6h6v-6zm10 0v12h5V18z"/></svg><h3>HOUSING</h3></div>
      <p>25% of renters are spending over 50% of income on rent. Especially bad locally; predatory leasing terms and skyrocketing rents. Proposed legislation is transforming HUD with the goal of getting rid of Section 8 housing that cares for vulnerable populations.</p>
    </div>
    <div class="topic">
      <div class="title"><svg viewBox="0 0 32 32"><path d="M16 1a15 15 0 0110 26l-2-2A12 12 0 0016 4zM6 5l2 2a12 12 0 008 21v3A15 15 0 016 5zm13-2l-9 15h6l-3 12 10-16h-6z"/></svg><h3>ENERGY</h3></div>
      <p>In 2022 Pine Hollow achieved 100% renewable energy in town buildings; this is now being destroyed by repeal of renewable energy project funding. Ridge College Innovation District prepares renewable workforce rules – all this is now in limbo.</p>
    </div>
    <div class="topic">
      <div class="title"><svg viewBox="0 0 32 32"><path d="M16 1a15 15 0 110 30 15 15 0 010-30zm0 2.5a12.5 12.5 0 00-12 9h24a12.5 12.5 0 00-12-9zM3.6 15a12.4 12.4 0 00.8 5h8.8a20 20 0 010-5zm12 1.5c3-4 9-5 12-4-1 6-5 11-12 11 2-3 4-5 7-7-3 1-6 3-7 5z"/></svg><h3>ENVIRONMENT</h3></div>
      <p>Reduced protections from coal ash pond leaks threaten public health. Corporations not held responsible for damage; public picks up the tab. Environmental Justice enforcement no longer a priority. Logging in Laurel County with no public oversight. It’s the “haz-mat” model: do nothing, wait for catastrophe, then fix it.</p>
    </div>
  </section>

  <section class="panel ballot-panel">
    <div class="panel-head"><h2>SAMPLE BALLOT RECOMMENDATIONS</h2></div>
    <ul class="ballot">
      <li><span class="bullet">★</span>US SENATE<span class="leader"></span><span class="choice">DANA WHITFIELD</span></li>
      <li><span class="bullet">★</span>US HOUSE – DISTRICT 5<span class="leader"></span><span class="choice">MARK DELANEY</span></li>
      <li><span class="bullet">★</span>REQMT TO SHOW ID FOR VOTERS NOT IN PERSON<span class="leader"></span><span class="choice">No</span></li>
      <li><span class="bullet">★</span>STATE SENATE – DISTRICT 47<span class="leader"></span><span class="choice">PAUL RENNER</span></li>
      <li><span class="bullet">★</span>HOUSE OF REPS – DISTRICT 93<span class="leader"></span><span class="choice">CARL MERCER</span></li>
      <li><span class="bullet">★</span>NC SUPREME COURT<span class="leader"></span><span class="choice">ALMA REYES</span></li>
      <li><span class="bullet">★</span>NC COURT OF APPEALS – SEAT 1<span class="leader"></span><span class="choice">JAMES HOLLOWAY</span></li>
      <li><span class="bullet">★</span>NC COURT OF APPEALS – SEAT 2<span class="leader"></span><span class="choice">TREVOR HAYNES</span></li>
      <li><span class="bullet">★</span>NC COURT OF APPEALS – SEAT 3<span class="leader"></span><span class="choice">CLAIRE WOZNIAK</span></li>
      <li><span class="bullet">★</span><span class="leader"></span></li>
      <li><span class="bullet">★</span><span class="leader"></span></li>
      <li><span class="bullet">★</span><span class="leader"></span></li>
      <li><span class="bullet">★</span><span class="leader"></span></li>
      <li><span class="bullet">★</span><span class="leader"></span></li>
      <li><span class="bullet">★</span><span class="leader"></span></li>
    </ul>
  </section>

  <footer class="footer-band">
    <span class="star" aria-hidden="true"><svg viewBox="0 0 24 24"><path d="M12 1l3.2 7.2 7.8.7-5.9 5.2 1.8 7.7L12 17.8l-6.9 4 1.8-7.7L1 8.9l7.8-.7z"/></svg></span>
    <p class="slogan">OUR COMMUNITY. <span class="future">OUR FUTURE.</span> <span class="vote">OUR VOTE</span>.</p>
    <span class="divider"></span>
    <p class="tagline"><span class="lead">Together,</span> we can build a better tomorrow.</p>
    <span class="star" aria-hidden="true"><svg viewBox="0 0 24 24"><path d="M12 1l3.2 7.2 7.8.7-5.9 5.2 1.8 7.7L12 17.8l-6.9 4 1.8-7.7L1 8.9l7.8-.7z"/></svg></span>
  </footer>
</div>
</body>
</html>
```